Business card design for new, innovative company - BluePlinth

We are a new company looking for a business card design that is fun, different and quirky. Must use corporate colour green - CMYK C:55, M:0, Y:100, K:0, and corporate colour grey - C:0, M:0, Y: 0, K:70.

We have developed the first real time data application, in which people are able to profile the data of their existing customers in order to pull out more good fit clients to direct their marketing activities at.

Industry/Entity Type

Marketing

Requirements
Must have
• Logo, name, title, telephone number, fax number, email, website, address

```html
<!DOCTYPE html>
<html lang="en">
<head>
<meta charset="utf-8">
<title>BluePlinth Business Card</title>
<link rel="stylesheet" href="https://fonts.googleapis.com/css2?family=Arimo:wght@400;700&family=Source+Sans+3:wght@400&display=swap">
<style>
  :root {
    --brand-green: #55ff00;
    --brand-grey: #5b6168;
    --text-grey: #454545;
    --paper: #ffffff;
    --edge: #000000;
  }
  * { margin: 0; padding: 0; box-sizing: border-box; }
  html, body {
    width: 1050px;
    height: 1200px;
    overflow: hidden;
    background: var(--paper);
  }
  .sheet {
    position: relative;
    width: 1050px;
    height: 1200px;
    border: 1px solid var(--edge);
    font-family: "Arimo", Arial, sans-serif;
  }
  .card-front {
    position: absolute;
    left: 0; top: 0;
    width: 1048px;
    height: 599px;
    background: var(--paper);
    border-bottom: 1px solid var(--edge);
  }
  .wordmark {
    position: absolute;
    left: 62px;
    top: 38px;
    font-size: 104px;
    font-weight: 700;
    letter-spacing: -3px;
    color: var(--brand-green);
    line-height: 1;
  }
  .person-name {
    position: absolute;
    left: 64px;
    top: 240px;
    font-size: 34px;
    font-weight: 700;
    color: var(--brand-green);
  }
  .contact-list, .address {
    position: absolute;
    left: 64px;
    font-size: 30px;
    color: var(--text-grey);
    line-height: 40px;
    list-style: none;
  }
  .contact-list { top: 302px; }
  .address { top: 481px; font-style: normal; }
  .accent-panel {
    position: absolute;
    left: 734px;
    top: 48px;
    width: 266px;
    height: 505px;
    border-radius: 24px;
    background: var(--brand-green);
  }
  .card-back {
    position: absolute;
    left: 0; top: 600px;
    width: 1048px;
    height: 598px;
    background: var(--brand-green);
  }
  .back-wordmark {
    position: absolute;
    left: 0; right: 0;
    top: 200px;
    text-align: center;
    font-size: 120px;
    font-weight: 700;
    letter-spacing: -3px;
    color: var(--paper);
    line-height: 1;
  }
  .website {
    position: absolute;
    left: 0; right: 0;
    top: 492px;
    text-align: center;
    font-family: "Source Sans 3", "Myriad Pro", sans-serif;
    font-size: 40px;
    color: var(--paper);
  }
</style>
</head>
<body>
  <main class="sheet">
    <section class="card-front">
      <div class="wordmark">BluePlinth</div>
      <h1 class="person-name">Jenna Colbourne</h1>
      <ul class="contact-list">
        <li>M: 07700900321</li>
        <li>T: 01632 960735</li>
        <li>E: jenna.colbourne@plinthdata.com</li>
      </ul>
      <address class="address">
        22c Fenmere Road<br>
        Wisbech, Cambridgeshire&nbsp; PE13 4XY
      </address>
      <div class="accent-panel"></div>
    </section>
    <section class="card-back">
      <div class="back-wordmark">BluePlinth</div>
      <div class="website">www.blueplinth.com</div>
    </section>
  </main>
</body>
</html>
```